Business Card Design For A Renovation Contractor Company

We need a business card for a new company based in Singapore, our company name is "KM Bravant". We are a renovation contractor that builds designs into reality. We build more of F&B restaurants, retail stores and commercial offices. We work very closely with designers. The final design should communicate to our client that we are a company that you can trust, that will plan and complete your project without giving you a headache. I like my client to remember my company as "KM". The beauty of SIMPLE is important.

Industry/Entity Type

Contractor

Requirements
Nice to have
• Black or Red base

```html
<!DOCTYPE html>
<html lang="en">
<head>
<meta charset="utf-8">
<title>KM Bravant – Business Card</title>
<link href="https://fonts.googleapis.com/css2?family=Montserrat:wght@400;500;600;700&display=swap" rel="stylesheet">
<style>
  :root {
    --stage: #2b2b2b;
    --card-dark: #231c20;
    --card-light: #f7f7f7;
    --red: #d8142a;
    --ink: #2a2a2a;
    --white: #ffffff;
    --muted: #cfcfcf;
  }
  * { box-sizing: border-box; margin: 0; padding: 0; }
  html, body { width: 1200px; height: 901px; overflow: hidden; }
  body {
    background: var(--stage);
    font-family: "Montserrat", sans-serif;
    display: flex;
    align-items: center;
    justify-content: center;
    gap: 50px;
  }
  .card {
    width: 525px;
    height: 300px;
    position: relative;
    border-radius: 2px;
    box-shadow: 0 10px 30px rgba(0,0,0,.45);
  }
  .card--front { background: var(--card-dark); color: var(--white); }
  .card--back { background: var(--card-light); color: var(--ink); }

  .brand {
    position: absolute;
    left: 50%;
    transform: translateX(-50%);
    display: flex;
    flex-direction: column;
    align-items: center;
    white-space: nowrap;
  }
  .brand__mark {
    border-radius: 50%;
    background: var(--red);
  }
  .brand__name {
    font-weight: 500;
    letter-spacing: .5px;
    line-height: 1;
    padding-bottom: 4px;
    border-bottom: 2px solid currentColor;
  }
  .brand__tagline {
    font-weight: 400;
    letter-spacing: .6px;
    margin-top: 4px;
  }
  .card--front .brand { top: 62px; }
  .card--front .brand__mark { width: 56px; height: 56px; margin-bottom: 12px; }
  .card--front .brand__name { font-size: 42px; color: var(--white); border-color: var(--muted); }
  .card--front .brand__tagline { font-size: 14px; color: var(--muted); }
  .website {
    position: absolute;
    bottom: 50px;
    width: 100%;
    text-align: center;
    font-size: 12px;
    font-weight: 600;
    color: var(--white);
  }

  .card--back .brand { top: 26px; }
  .card--back .brand__mark { width: 38px; height: 38px; margin-bottom: 8px; }
  .card--back .brand__name { font-size: 30px; color: var(--ink); }
  .card--back .brand__tagline { font-size: 10px; color: var(--ink); }

  .person {
    position: absolute;
    left: 44px;
    bottom: 38px;
  }
  .person__name { color: var(--red); font-size: 18px; font-weight: 600; }
  .person__role { font-size: 12px; font-weight: 600; margin-bottom: 16px; }
  .contact { font-size: 13px; line-height: 1.6; font-weight: 500; }
  .contact dt { color: var(--red); font-weight: 600; display: inline-block; width: 56px; }
  .contact dd { display: inline; }
  .address {
    position: absolute;
    right: 40px;
    top: 168px;
    font-size: 13px;
    line-height: 1.6;
    font-weight: 500;
    font-style: normal;
  }
  .address__label { color: var(--red); font-weight: 600; }
</style>
</head>
<body>
  <section class="card card--front">
    <div class="brand">
      <span class="brand__mark"></span>
      <span class="brand__name">KM Bravant</span>
      <span class="brand__tagline">turning every plan into space</span>
    </div>
    <p class="website">www.kmbravant.com</p>
  </section>

  <section class="card card--back">
    <div class="brand">
      <span class="brand__mark"></span>
      <span class="brand__name">KM Bravant</span>
      <span class="brand__tagline">turning every plan into space</span>
    </div>
    <div class="person">
      <p class="person__name">Marcus Lim</p>
      <p class="person__role">Position Director</p>
      <dl class="contact">
        <div><dt>Phone</dt><dd>6123 4567</dd></div>
        <div><dt>Cell</dt><dd>9123 4567</dd></div>
        <div><dt>Email</dt><dd>marcus@kmbravant.com</dd></div>
      </dl>
    </div>
    <address class="address">
      <span class="address__label">Address</span> 18 Telok Ayer Street<br>
      #03-12 Ayer Hub<br>
      Singapore 048620
    </address>
  </section>
</body>
</html>
```